Research, Writing and Editing business needs a Business Card Design

I need a business card design for a new company based in Melbourne called The Bellwood Advisory Group. We provide research, writing and editing services. The company logo is attached, but I am open to your creative designs for business cards with the logo. As you will note, there are two potential logos. Feel free to use either of the logos.

The overall look I am hoping for is sleek, sophisticated, feminine and elegant.

Thanks in advance for your efforts.

Target Market(s)

Business professionals, academics and students

Industry/Entity Type

Business

Font styles to use
Serif
Script

Colors

Designer to choose colors to be used in the design.

Requirements
Must have
• The Bellwood Advisory Group
Dr Tessa Brennig

M: 0458 293 647
E: tessa@thebellwoodadvisorygroup.com.au
W: thebellwoodadvisorygroup.com.au
Nice to have
• Research | Writing | Editing

```html
<!DOCTYPE html>
<html lang="en">
<head>
<meta charset="utf-8">
<title>The Bellwood Advisory Group – Business Card</title>
<link href="https://fonts.googleapis.com/css2?family=Tinos&display=swap" rel="stylesheet">
<style>
  :root {
    --backdrop: #6b5a4a;
    --paper-light: #f5f2ed;
    --paper-mid: #ebe6de;
    --paper-edge: #d8d0c4;
    --ink: #1c1c1c;
    --ink-soft: #2a2a2a;
  }
  * { margin: 0; padding: 0; box-sizing: border-box; }
  html, body {
    width: 1200px;
    height: 1200px;
    overflow: hidden;
    background: var(--backdrop);
  }
  .canvas {
    position: relative;
    width: 1200px;
    height: 1200px;
    font-family: "Tinos", "Times New Roman", serif;
    color: var(--ink);
  }
  .card {
    position: absolute;
    left: 138px;
    width: 924px;
    height: 566px;
    background: radial-gradient(ellipse at 50% 40%, var(--paper-light) 0%, var(--paper-mid) 60%, var(--paper-edge) 100%);
    box-shadow: 0 4px 14px rgba(0, 0, 0, 0.35);
  }
  .card--front { top: 18px; }
  .card--back { top: 612px; }

  .wordmark {
    position: absolute;
    display: flex;
    align-items: center;
    gap: 18px;
    color: var(--ink);
    text-transform: uppercase;
    white-space: nowrap;
  }
  .wordmark__square {
    display: block;
    background: var(--ink);
  }
  .card--front .wordmark {
    left: 0;
    right: 0;
    top: 238px;
    justify-content: center;
    font-size: 32px;
    letter-spacing: 4px;
  }
  .card--front .wordmark__square { width: 44px; height: 44px; }

  .card--back .wordmark {
    left: 58px;
    top: 120px;
    font-size: 21px;
    letter-spacing: 2px;
    gap: 14px;
  }
  .card--back .wordmark__square { width: 34px; height: 34px; }

  .holder-name {
    position: absolute;
    right: 78px;
    top: 124px;
    font-size: 24px;
    color: var(--ink-soft);
  }
  .contact-list {
    position: absolute;
    left: 56px;
    top: 362px;
    list-style: none;
    font-size: 20px;
    line-height: 35px;
    color: var(--ink-soft);
  }
  .services {
    position: absolute;
    left: 0;
    right: 0;
    top: 510px;
    display: flex;
    align-items: center;
    gap: 14px;
    font-size: 24px;
    color: var(--ink-soft);
  }
  .services__rule {
    flex: 1;
    height: 2px;
    background: var(--ink);
  }
</style>
</head>
<body>
<main class="canvas">
  <section class="card card--front">
    <div class="wordmark">
      <span class="wordmark__square"></span>
      <span class="wordmark__name">The Bellwood Advisory Group</span>
    </div>
  </section>

  <section class="card card--back">
    <div class="wordmark">
      <span class="wordmark__square"></span>
      <span class="wordmark__name">The Bellwood Advisory Group</span>
    </div>
    <p class="holder-name">Dr Tessa Brennig</p>
    <ul class="contact-list">
      <li>Mobile: 0458 293 647</li>
      <li>Email: tessa@thebellwoodadvisorygroup.com.au</li>
      <li>Web: thebellwoodadvisorygroup.com.au</li>
    </ul>
    <div class="services">
      <span class="services__rule"></span>
      <span class="services__text">Research | Writing | Editing</span>
      <span class="services__rule"></span>
    </div>
  </section>
</main>
</body>
</html>
```